Fine Art business needs new website

We need a simple website with a home page, about us page, New sculptures, Sold sculptures, and a contact us page.Our sculptures are very high end one of a kind pieces. As such we need the site to be VERY elegant and professional. Lastly, because I'll be updating pictures on the website on a monthly basis it needs to be user friendly to update (Wordpress is preferred). The only branding we have so far for the business is a business card.
Updates
I wasn't completely ready when this project launched, also I am on the road right now and haven't been able to be as responsive to all you designers as I would like. I will work on giving feedback to all the top designs we've received so far. Thank you all so much for your participation and hardwork.
Target Market(s)
High end customers (affluent), art collectors, interior decorators/designers
Industry/Entity Type
Art Gallery
Coding
Coded - Design and coding required
Number of Pages Required
5+ page
Requirements
Must have
- Easily editable picture gallery for myself so that I can add new pieces(pictures of the pieces), remove sold pieces, etc. I would like the website to be built in wordpress so I can update it. I currently use tendsitehub through Hostwick for my other business website and would like to do the same for this one.
- Pages:
- -Intro page with featured pieces
- -Current pieces gallery (for sale) mainly a picture gallery
- -Sculptures archive (sold pieces) another picture gallery
- -About us: Pull-down of -about the artist (attached content)
- -Artistic Process (attached content)
- -Show Schedule:
- -one page dedicated to "friends of OKW" (basically a link page)
- TO BE CLEAR "www.brindlelads.example" IS A TOTALLY DIFFERENT SITE AND I'M NOT TRYING TO COMBINE THE TWO OR JOIN THEM INTO ONE. This page needs be more elegant and seperate from the Brindle Lads site.
- UPDATE: I'd like a link to the OKW Chatterly page: https://www.chatterly.example/orvanekilnworks/
Nice to have
- I would like the pictures on the gallery pages able to have text connected with them (Materials, price)
- I would like the site style and fonts to be similar to our business cards we've already had designed (picture attached).
Should not have
- Too much flash or other things that will make the site slow to load.

```html
<!DOCTYPE html>
<html lang="en">
<head>
<meta charset="utf-8">
<title>Orvane Kiln Works — Sculptures Archive</title>
<link rel="stylesheet" href="https://fonts.googleapis.com/css2?family=EB+Garamond:ital,wght@0,400;0,500;0,700;1,700&display=swap">
<style>
:root{
  --ink:#3a3a3a;
  --ink-soft:#555;
  --paper:#ffffff;
  --tile:#1b1b1b;
  --label:#ffffff;
  --price:#cfcfcf;
  --footer:#1f1f1f;
  --footer-base:#141414;
  --footer-text:#e8e8e8;
  --footer-rule:#555;
  --card:#ffffff;
  --plinth:#2c1a17;
  --geode-blue:#8a98d0;
  --geode-blue-deep:#3e4570;
  --amethyst:#8e5ad6;
  --amethyst-deep:#40236e;
  --agate:#a8704a;
  --agate-deep:#4a2c1c;
}
*{box-sizing:border-box;margin:0;padding:0}
html,body{width:1200px;height:2542px;overflow:hidden;background:var(--paper)}
body{font-family:"EB Garamond",Georgia,serif;color:var(--ink);position:relative}
.site-header{position:absolute;top:0;left:0;width:1200px;text-align:center}
.brand{position:absolute;top:22px;width:100%;font-size:33px;font-weight:400;letter-spacing:1.5px;color:var(--ink)}
.main-nav{position:absolute;top:89px;width:100%;display:flex;justify-content:center;gap:28px;font-size:11.5px;letter-spacing:.2px}
.main-nav a{color:var(--ink-soft);text-decoration:none;padding-bottom:4px}
.main-nav a.is-current{border-bottom:1.5px solid var(--ink)}
.page-title{position:absolute;top:206px;width:1200px;text-align:center;font-size:60px;font-weight:400;letter-spacing:2px;color:var(--ink)}
.category{position:absolute;left:0;width:1200px}
.category-title{text-align:center;font-size:25px;font-weight:400;letter-spacing:1px;color:var(--ink-soft);height:40px;line-height:40px}
.gallery{display:flex;gap:10px;justify-content:center;margin-top:36px}
.piece{position:relative;width:288px;height:394px;background:var(--tile);overflow:hidden}
.piece-photo{position:absolute;inset:0}
.photo-geode{background:
  radial-gradient(ellipse 26% 46% at 48% 44%,var(--geode-blue) 0%,var(--geode-blue-deep) 45%,rgba(27,27,27,0) 80%),
  linear-gradient(to bottom,var(--tile) 0 76%,var(--plinth) 82%,#120c0b 100%)}
.photo-amethyst{background:
  radial-gradient(ellipse 32% 46% at 54% 42%,var(--amethyst) 0%,var(--amethyst-deep) 48%,rgba(27,27,27,0) 82%),
  linear-gradient(to bottom,var(--tile) 0 76%,var(--plinth) 82%,#120c0b 100%)}
.photo-agate{background:
  radial-gradient(ellipse 24% 44% at 56% 38%,var(--agate) 0%,var(--agate-deep) 48%,rgba(27,27,27,0) 82%),
  linear-gradient(to bottom,var(--tile) 0 76%,var(--plinth) 82%,#120c0b 100%)}
.piece-name{position:absolute;left:19px;top:24px;background:var(--label);color:#222;font-size:13px;padding:3px 12px;height:26px;line-height:20px}
.piece-price{position:absolute;left:19px;top:50px;background:var(--price);color:#222;font-size:13px;padding:3px 12px;height:25px;line-height:19px;width:72px}
.view-more{display:block;text-align:center;margin-top:36px;font-size:12px;color:var(--ink-soft);text-decoration:underline}
.site-footer{position:absolute;top:2127px;left:0;width:1200px;height:380px;background:var(--footer);color:var(--footer-text)}
.footer-col{position:absolute;top:36px}
.footer-col h2{font-size:17px;font-weight:400;letter-spacing:.8px;margin-bottom:24px;white-space:nowrap}
.show{font-size:13px;margin-bottom:14px;line-height:1.3}
.show em{display:block;font-weight:700;font-style:italic;font-size:13px}
.rule{border-top:1px solid var(--footer-rule);margin:6px 0 12px}
.footer-link{color:var(--footer-text);font-size:13px;text-decoration:underline}
.note{font-size:13px;margin-bottom:14px}
.post{width:180px;background:var(--card);color:#222;padding:8px;font-family:Arial,sans-serif;font-size:9px;line-height:1.35;margin-bottom:16px}
.post-head{display:flex;align-items:center;gap:6px;margin-bottom:6px}
.post-avatar{width:20px;height:20px;background:#777}
.post-head b{display:block;font-size:9px}
.post-head small{color:#888;font-size:7px}
.post-badge{margin-left:auto;width:11px;height:11px;background:#3b5998;align-self:flex-start}
.contact p{font-size:13px;line-height:1.3;margin-bottom:12px}
.social{display:flex;gap:4px;margin-bottom:14px}
.social span{width:11px;height:11px;background:var(--footer-text)}
.newsletter{display:flex;margin-top:4px}
.newsletter input{width:150px;height:23px;border:none;background:#fff}
.newsletter button{width:54px;height:23px;border:none;border-left:1px solid #ccc;background:#fff;font-family:inherit;font-size:10px}
.footer-base{position:absolute;top:2507px;left:0;width:1200px;height:35px;background:var(--footer-base);color:#999;font-size:9px;text-align:center;line-height:35px}
</style>
</head>
<body>
<header class="site-header">
  <div class="brand">ORVANE KILN WORKS</div>
  <nav class="main-nav">
    <a href="#">HOME</a><a href="#">ABOUT US</a><a href="#">CURRENT PIECES</a><a href="#" class="is-current">SCULPTURES ARCHIVE</a><a href="#">BRINDLELADS</a><a href="#">CONTACT US</a>
  </nav>
</header>

<h1 class="page-title">SCULPTURES ARCHIVE</h1>

<section class="category" style="top:342px">
  <h2 class="category-title">CATEGORY 1</h2>
  <div class="gallery">
    <article class="piece"><div class="piece-photo photo-geode" role="img" aria-label="Photo of a blue crystal geode sculpture on a dark pedestal"></div><div class="piece-name">PRODUCT NAME</div><div class="piece-price">$2950</div></article>
    <article class="piece"><div class="piece-photo photo-amethyst" role="img" aria-label="Photo of a purple amethyst sculpture on a stone base"></div><div class="piece-name">PRODUCT NAME</div><div class="piece-price">$2950</div></article>
    <article class="piece"><div class="piece-photo photo-agate" role="img" aria-label="Photo of an amber agate slice sculpture on a dark stand"></div><div class="piece-name">PRODUCT NAME</div><div class="piece-price">$2950</div></article>
  </div>
  <a class="view-more" href="#">VIEW MORE</a>
</section>

<section class="category" style="top:914px">
  <h2 class="category-title">CATEGORY 2</h2>
  <div class="gallery">
    <article class="piece"><div class="piece-photo photo-geode" role="img" aria-label="Photo of a blue crystal geode sculpture on a dark pedestal"></div><div class="piece-name">PRODUCT NAME</div><div class="piece-price">$2950</div></article>
    <article class="piece"><div class="piece-photo photo-amethyst" role="img" aria-label="Photo of a purple amethyst sculpture on a stone base"></div><div class="piece-name">PRODUCT NAME</div><div class="piece-price">$2950</div></article>
    <article class="piece"><div class="piece-photo photo-agate" role="img" aria-label="Photo of an amber agate slice sculpture on a dark stand"></div><div class="piece-name">PRODUCT NAME</div><div class="piece-price">$2950</div></article>
  </div>
  <a class="view-more" href="#">VIEW MORE</a>
</section>

<section class="category" style="top:1492px">
  <h2 class="category-title">CATEGORY 3</h2>
  <div class="gallery">
    <article class="piece"><div class="piece-photo photo-geode" role="img" aria-label="Photo of a blue crystal geode sculpture on a dark pedestal"></div><div class="piece-name">PRODUCT NAME</div><div class="piece-price">$2950</div></article>
    <article class="piece"><div class="piece-photo photo-amethyst" role="img" aria-label="Photo of a purple amethyst sculpture on a stone base"></div><div class="piece-name">PRODUCT NAME</div><div class="piece-price">$2950</div></article>
    <article class="piece"><div class="piece-photo photo-agate" role="img" aria-label="Photo of an amber agate slice sculpture on a dark stand"></div><div class="piece-name">PRODUCT NAME</div><div class="piece-price">$2950</div></article>
  </div>
  <a class="view-more" href="#">VIEW MORE</a>
</section>

<footer class="site-footer">
  <div class="footer-col" style="left:159px;width:180px">
    <h2>UPCOMING SHOWS</h2>
    <div class="show">Art Fair Cedar Basin<em>August 2018</em></div>
    <div class="show">Silverpine Fine Art Show<em>July 2018</em></div>
    <div class="show">Marlow Park Arts and<br>Music Festival<em>June 2018</em></div>
    <div class="show">Redstone Creek Festival<em>May 2018</em></div>
    <div class="rule"></div>
    <a class="footer-link" href="#">View All</a>
  </div>
  <div class="footer-col" style="left:380px;width:176px">
    <h2>UPCOMING EVENTS</h2>
    <p class="note">There are no upcoming events yet</p>
    <div class="rule"></div>
    <a class="footer-link" href="#">View Calender</a>
  </div>
  <div class="footer-col" style="left:615px;width:180px">
    <h2>CHATTERLY</h2>
    <div class="post">
      <div class="post-head"><span class="post-avatar"></span><span><b>The Brindle Lads</b><small>10 hours ago</small></span><span class="post-badge"></span></div>
      Geode fans, announcing a flash sale, free shipping on all CRAFTLY orders for the next two weeks!!<br>*Minimum $25 order
    </div>
    <div class="post">
      <div class="post-head"><span class="post-avatar"></span><span><b>The Brindle Lads</b><small>about a week ago</small></span><span class="post-badge"></span></div>
      Few more new products. First a crystal canyon geode, then a THUNDEREGG! Both will be available on our Craftly store in the next week.
    </div>
    <div class="rule"></div>
    <a class="footer-link" href="#">Goto Chatterly Page</a>
  </div>
  <div class="footer-col contact" style="left:837px;width:204px">
    <h2>CONTACT US</h2>
    <p>The Brindle Lads, PO box 40218<br>Pinecrest Hollow CO 80999</p>
    <p>hello@brindlelads.example</p>
    <p>+1.555.014.2270</p>
    <div class="social"><span></span><span></span><span></span><span></span><span></span><span></span><span></span></div>
    <div class="rule"></div>
    <h2 style="margin-top:20px;margin-bottom:10px">NEWSLETTER</h2>
    <form class="newsletter"><input type="email" aria-label="Email address"><button type="button">Send</button></form>
  </div>
</footer>
<div class="footer-base">Copyright © 2018 The Brindle Lads</div>
</body>
</html>
```